Security Company Needs a Website *

We need a website that gives our clients information about the services we provide, methods of contacting us and landing page to advertise on social media sites.

We need five landing pages titled Home, About Us, Services, Contact Us and a Landing Page that can be linked to Chatterlane advertising.

About Us - Should have a section for Core Values & Ethics, Our Vision, Our Mission and Partners.

Services - This page should show the different categories which include CCTV, Security Alarms, Access Control and Fire Protection.

CCTV Service Description:
Closed circuit television (CCTV) has long been implemented by businesses as a surveillance tool in areas that need monitoring. With digital CCTV cameras, multiple video cameras transmit signals through a set of monitors. The cameras provide thorough surveillance of the area.

With vast technological improvements over the last ten years, businesses with CCTV systems can use unique IP cameras and video analytics to monitor traffic flows, people-count, implement facial and number plate recognition. Useful information about customer behaviour and demographics can be discovered too. CCTV helps prevent crime in many industries and can assist with the improvement of industrial processes, safety on transport systems and traffic monitoring.

Security Alarms Service Description:
Alarms systems are electronic devices programmed to alert people to specific dangers and detect intrusions, fire or theft. Security alarms, systems and access control monitoring combine to create an integrated surveillance solution, tailored to your business’ unique requirements. Our surveillance and alarm monitoring services are ideal for perimeter protection from unwanted intruders or potential dangers.

Access Control Services:
An access control system allows for the free flow of authorised personnel while denying entry to unwanted visitors. With walk-in thieves and trespassers shut out, you dramatically reduce your exposure to crime while increasing the security of your employees, visitors, information and assets.

* Control when and who is entering your premises
* Protect employees, assets and information
* Secure an area or sector
* Observe movement
* Integrate with other security systems

Our range of access control systems can be seamlessly linked to other systems in our portfolio. These include Fire Detection Systems, Intruder Alarms, CCTV, and Building Management. A common request involves the need for a CCTV camera to pan around and focus on a door that has been highlighted as a security risk by the access control system.

Fire Protection Service:
To Be Advised

The above copy-writing will also have to be changed.

Contact Us - This form needs to be simple and straightforward to gather the prospects information and we would like to have a call to action on this page. The Contact Us page should also have a wayfindr plot location of our office address.

We would also like to have a link to our chatterlane page on the website.

Target Market(s)

Commercial businesses, building construction developers and property managers.

Industry/Entity Type

Security

Number of Pages Required

5+ page

Font styles to use
Sans Serif

Colors

Designer to choose colors to be used in the design.

Requirements
Must have
• We need to have the same look and feel as well as website features as the following website:
• https://www.kovrangard.com.au/business-security/
• The website must be easy to use and easy to edit as well.

```html
<!DOCTYPE html>
<html lang="en">
<head>
<meta charset="utf-8">
<title>About Us – Halvern Security</title>
<link href="https://fonts.googleapis.com/css2?family=Poppins:wght@300;400;500;600;700&display=swap" rel="stylesheet">
<style>
:root{
  --navy:#1e1a5c;
  --brand-blue:#0a6aad;
  --nav-active:#2b3a8a;
  --call-blue:#1d4b8f;
  --text-grey:#8a8a8a;
  --text-dark:#555;
  --section-grey:#f3f3f3;
  --footer-dark:#111114;
  --footer-text:#8c8c8c;
  --link-blue:#3d8ef0;
  --white:#fff;
}
*{margin:0;padding:0;box-sizing:border-box}
html,body{width:1200px;height:1170px;overflow:hidden}
body{font-family:'Poppins',sans-serif;background:var(--white);position:relative}
.abs{position:absolute}

/* header */
.site-header{position:absolute;left:0;top:0;width:1200px;height:65px;background:var(--white)}
.brand{position:absolute;left:154px;top:8px;display:flex;align-items:center;gap:12px}
.brand-dot{width:50px;height:50px;border-radius:50%;background:var(--nav-active)}
.brand-name{font-size:19px;font-weight:400;color:var(--navy);letter-spacing:.2px}
.call{position:absolute;left:894px;top:10px;color:var(--call-blue);font-weight:600;font-size:16.5px;line-height:22px}

.main-nav{position:absolute;left:0;top:65px;width:1200px;height:37px;background:var(--brand-blue)}
.nav-list{position:absolute;left:154px;top:0;display:flex;height:37px;list-style:none;border-left:1px solid rgba(0,0,0,.12)}
.nav-list li{height:37px;display:flex;align-items:center;padding:0 21px;color:var(--white);font-size:13.5px;font-weight:500;border-right:1px solid rgba(0,0,0,.12)}
.nav-list li.active{background:var(--nav-active);padding:0 24px}
.search{position:absolute;left:838px;top:0;width:208px;height:37px;border-left:1px solid rgba(0,0,0,.12);border-right:1px solid rgba(0,0,0,.12);color:rgba(255,255,255,.6);font-size:11px;padding:11px 16px}
.search svg{position:absolute;right:14px;top:11px}

/* about */
.page-title{position:absolute;left:0;width:1200px;top:124px;text-align:center;font-size:23.5px;font-weight:600;color:var(--navy)}
.title-rule{position:absolute;left:579px;top:155px;width:42px;height:1px;background:var(--navy)}
.lead{position:absolute;left:245px;width:710px;text-align:center;font-size:13.3px;font-weight:300;line-height:20.8px;color:var(--text-grey)}

.grey-band{position:absolute;left:0;top:306px;width:1200px;height:495px;background:var(--section-grey)}
.sub-title{position:absolute;left:0;width:1200px;text-align:center;font-size:16px;font-weight:400;color:var(--navy)}
.team-photo{position:absolute;left:152px;top:418px;width:447px;height:240px;background:linear-gradient(120deg,#d9cdb8 0%,#a58a66 35%,#5b4733 60%,#2a3550 85%,#1d2438 100%)}
.values-title{position:absolute;left:643px;top:426px;font-size:16px;color:var(--navy)}
.values{position:absolute;left:643px;top:459px;list-style:none}
.values li{height:27.2px;display:flex;align-items:center;font-size:13.3px;font-weight:300;color:var(--text-dark)}
.values li::before{content:"";width:5px;height:5px;border:2px solid #aaa;border-radius:50%;margin:0 13px 0 1px}
.values li.first::before{border-color:var(--navy)}
.mission{color:var(--text-dark)}

/* footer */
.site-footer{position:absolute;left:0;top:801px;width:1200px;height:369px;background:linear-gradient(115deg,#0b0b0d 0%,#131316 45%,#1c1c20 46%,#141418 100%)}
.f-title{position:absolute;left:153px;top:22px;font-size:23.5px;font-weight:700;color:var(--white)}
.f-rule{position:absolute;left:155px;top:52px;width:48px;height:1px;background:var(--white)}
.field{position:absolute;border:1px solid #6b6b6b;color:#7a7a7a;font-size:11.5px;font-weight:300;padding:5px 9px}
.send{position:absolute;left:153px;top:288px;color:var(--white);font-size:13px;font-weight:600;display:flex;align-items:center;gap:10px}
.col-title{position:absolute;top:80px;font-size:17.5px;font-weight:600;color:var(--white)}
.contact-item{position:absolute;left:647px;display:flex;gap:12px;color:var(--white);font-size:12px;font-weight:400}
.contact-value{position:absolute;left:672px;font-size:11.5px;font-weight:300;color:var(--footer-text)}
.quick{position:absolute;left:904px;top:116px;list-style:none}
.quick li{height:26.4px;font-size:11.5px;font-weight:300;color:var(--footer-text)}
.f-line{position:absolute;left:153px;top:332px;width:891px;height:1px;background:#333}
.copy{position:absolute;left:153px;top:343px;font-size:11.5px;color:var(--white);font-weight:300}
.copy span{color:var(--link-blue)}
.social{position:absolute;right:155px;top:344px;display:flex;gap:14px;list-style:none}
.social li{font-size:10px;color:var(--white);font-weight:500}
</style>
</head>
<body>

<header class="site-header">
  <div class="brand"><span class="brand-dot"></span><span class="brand-name">HALVERN SECURITY</span></div>
  <div class="call">Call Us Now<br>(040) 71830 44102</div>
</header>

<nav class="main-nav">
  <ul class="nav-list">
    <li>Home</li>
    <li class="active">About Us</li>
    <li>Services</li>
    <li>Contact&nbsp; Us</li>
  </ul>
  <div class="search">Search
    <svg width="14" height="14" viewBox="0 0 14 14"><circle cx="6" cy="6" r="4.5" fill="none" stroke="rgba(255,255,255,.6)" stroke-width="1.6"/><line x1="9.3" y1="9.3" x2="13" y2="13" stroke="rgba(255,255,255,.6)" stroke-width="1.8"/></svg>
  </div>
</nav>

<main>
  <h1 class="page-title">About Us</h1>
  <div class="title-rule"></div>
  <p class="lead" style="top:173px">Lorem ipsum dolor sit amet, consectetur adipiscing elit, sed do eiusmod tempor incididunt ut labore et dolore magna aliqua. Ut enim ad minim veniam, quis nostrud exercitation ullamco laboris nisi ut aliquip ex ea commodo consequat. Duis aute irure dolor in reprehenderit in voluptate velit esse cillum dolore eu fugiat nulla pariatur. ullamco laboris nisi ut aliquip ex ea commodo consequat. Duis aute irure dolor in reprehenderit in voluptate velit esse cillum dolore eu fugiat nulla pariatur.</p>

  <section class="grey-band"></section>
  <h2 class="sub-title" style="top:326px">Our Vision</h2>
  <p class="lead" style="top:355px">Lorem ipsum dolor sit amet, consectetur adipiscing elit, sed do eiusmod tempor incididunt ut labore et dolore magna aliqua. Ut enim ad minim veniam, quis nostrud exercitation ullamco</p>

  <div class="team-photo" role="img" aria-label="Photo of colleagues reviewing documents at a wooden desk"></div>
  <h2 class="values-title">Core Values &amp; Ethics</h2>
  <ul class="values">
    <li class="first">Lorem ipsum dolor sit amet, consectetur</li>
    <li>Consectetur adipiscing elit</li>
    <li>tempor incididunt ut labore et dolore</li>
    <li>Lorem ipsum dolor sit amet, consectetur</li>
    <li>Consectetur adipiscing elit</li>
    <li>tempor incididunt ut labore et dolore</li>
    <li>Consectetur adipiscing elit</li>
  </ul>

  <h2 class="sub-title" style="top:680px">Our Mission</h2>
  <p class="lead mission" style="top:713px">Lorem ipsum dolor sit amet, consectetur adipiscing elit, sed do eiusmod tempor incididunt ut labore et dolore magna aliqua. Ut enim ad minim veniam, quis nostrud exercitation ullamco laboris nisi ut aliquip ex ea commodo consequat. Duis aute irure dolor in reprehenderit i</p>
</main>

<footer class="site-footer">
  <h2 class="f-title">Contact Us</h2>
  <div class="f-rule"></div>

  <div class="field" style="left:152px;top:82px;width:218px;height:27px">Name</div>
  <div class="field" style="left:390px;top:82px;width:217px;height:27px">Email</div>
  <div class="field" style="left:152px;top:127px;width:218px;height:27px">Phone</div>
  <div class="field" style="left:390px;top:127px;width:217px;height:27px">Company</div>
  <div class="field" style="left:152px;top:173px;width:455px;height:103px;padding:8px 11px">Message</div>
  <div class="send"><svg width="13" height="8" viewBox="0 0 13 8"><line x1="0" y1="4" x2="12" y2="4" stroke="#fff" stroke-width="1.2"/><polyline points="8.5,0.8 12,4 8.5,7.2" fill="none" stroke="#fff" stroke-width="1.2"/></svg>Send Now</div>

  <h3 class="col-title" style="left:647px">Get in Touch</h3>
  <div class="contact-item" style="top:116px">
    <svg width="13" height="12" viewBox="0 0 13 12"><path d="M6.5 0.5 L12.5 6 H10.5 V11.5 H7.8 V8 H5.2 V11.5 H2.5 V6 H0.5 Z" fill="#fff"/></svg>Office Address</div>
  <div class="contact-value" style="top:143px">58 Marrow Lane, Eastbrook, UK</div>
  <div class="contact-item" style="top:174px">
    <svg width="14" height="11" viewBox="0 0 14 11"><rect x="0.7" y="0.7" width="12.6" height="9.6" fill="none" stroke="#fff" stroke-width="1.2"/><polyline points="0.7,0.7 7,6 13.3,0.7" fill="none" stroke="#fff" stroke-width="1.2"/></svg>Email</div>
  <div class="contact-value" style="top:198px">hello@halvernsecurity.test</div>
  <div class="contact-item" style="top:226px">
    <svg width="13" height="13" viewBox="0 0 13 13"><path d="M2.5 0.8 L4.8 3.5 L3.6 5 Q5.2 8 8 9.4 L9.5 8.2 L12.2 10.5 L10.6 12.3 Q5.5 12 1 3 Z" fill="#fff"/></svg>Phone</div>
  <div class="contact-value" style="top:251px">(040) 71830 44187</div>

  <h3 class="col-title" style="left:902px">Quick links</h3>
  <ul class="quick">
    <li>Home</li><li>About Us</li><li>Services</li><li>FAQ</li><li>Customer Support</li><li>Privacy Polacy</li>
  </ul>

  <div class="f-line"></div>
  <p class="copy">© Copyright 2018 - <span>Halvern Security</span> - All right reserved.</p>
  <ul class="social">
    <li>Chatterlane</li><li>Chirpwire</li><li>Proflink</li><li>Circleplus</li>
  </ul>
</footer>

</body>
</html>
```